Web design for a pet services marketplace

I represent a South American based company: “PERUMIS” which provides a different array of pet related services. As a starting point, I would like to get proposals for 1 page website (plus a general frame for forms, instructions etc) web design job for a dog boarding marketplace. If you could add a logo is desirable.
By a Dog Boarding Marketplace, I mean a community marketplace, very much like an roomlyx, but for pet services (initially dog boarding/daycare, but evolving to other services such as dog walkers. The purpose is to bring together dog owners and dog-care providers according to qualifications or characteristics given at time of input and needs of the dog owner given at the time of searching. Providers create a profile, entering certain information requested in forms such as their location, type of house/apt, what type/size of dogs they take, prior experience, as well as a personal introduction and pictures. Providers will set their own rates and calendar availability. Then customers browse, schedule and book and pay online. As it works for similar services, there will be a system of reviews and feedback for each care provider.
As to the website, it should be substantially similar to the following websites: (www.pawstaylo.example , www.kinbrel.example). It should be simple and straightforward, prioritizing ease of use. I would like for visitors to easily understand how the model works by seeing the home page, and getting pop up explanations by browsing over each main icon or message on the homepage. Therefore, I would try to keep additional pages to a minimum.
As I’m new to this, I would not venture as to how many pages I would need and would defer to your suggestion, according to the examples provided. However, I would like to have a visually striking front end, with dog related pictures or cartoon type images. Icons etc should be fun, and related to dogs, vacations, hotels/lodging, travel, etc. Secondary pages (like enrollment forms, Q&A, etc) could have a clean design, maybe adding some non-obtrusive related imagery.
Please note that attached pictures are , third party property and are for guide only.
Additional info:
In general I want to make a site very much like the examples of pawstaylo and kinbrel, but i think a better job could be done in terms of design. Please feel free to provide your own ideas.
1. For now, since the site will be new, we would not be including a testimonials section. However, we could use the space , or maybe smaller, with the "spread the love"section for announcing special deals for people who share the project.
2. In the principal section, I would like to see a clean layout. Much like pawstaylo does. As an alternative, I would also like to see how it would look like if we handled more cartoon type drawings instead of pictures (just a suggestion to see how it would look like).
3. Search spaces should be more floating (merging more with background), as in pawstaylo, not in larger boxes.
Updates
Please find in the attachments a very rough wire frame that i just did as response to a project proposal. Please note where i say OK (top and bottom) I mean that those two sections i found ok in such project or the model websites. Pretty regular content in those sections. Added Friday, July 10, 2015
Target Market(s)
dog owners, people who are willing to host pets in their home, kennels
Industry/Entity Type
Pet Care
Number of Pages Required
1 page

```html
<!DOCTYPE html>
<html lang="en">
<head>
<meta charset="utf-8">
<title>Perumis – Find a Loving Dog Sitter</title>
<link rel="stylesheet" href="https://fonts.googleapis.com/css2?family=Open+Sans:wght@400;600;700;800&display=swap">
<style>
:root{
  --green:#6cb33f;
  --green-dark:#4f8f2a;
  --orange:#f26522;
  --ink:#333333;
  --muted:#6b6b6b;
  --beige:#efecdc;
  --footer:#2c2c2c;
  --footer-base:#1f1f1f;
  --line:#d9d9d9;
  --white:#ffffff;
}
*{box-sizing:border-box;margin:0;padding:0}
html,body{width:1200px;height:2420px;overflow:hidden}
body{font-family:"Open Sans",Arial,sans-serif;color:var(--ink);background:var(--white);position:relative}
a{color:inherit;text-decoration:none}

/* Header */
.site-header{position:absolute;top:0;left:0;width:1200px;height:68px;background:var(--white);display:flex;align-items:center;padding:0 130px;border-bottom:1px solid #eee}
.brand{display:flex;align-items:center;gap:10px;font-weight:800;font-size:30px;color:var(--green)}
.brand-dot{width:22px;height:22px;border-radius:50%;background:var(--green)}
.main-nav{display:flex;gap:24px;margin-left:50px;font-size:14px;font-weight:600}
.user-nav{margin-left:auto;display:flex;align-items:center;gap:22px;font-size:14px;font-weight:600}
.btn{display:inline-block;border-radius:3px;color:var(--white);font-weight:600;font-size:14px}
.btn-green{background:var(--green)}
.btn-orange{background:var(--orange)}
.user-nav .btn{padding:7px 16px}

/* Hero */
.hero{position:absolute;top:68px;left:0;width:1200px;height:472px}
.hero-photo{position:absolute;inset:0;background:linear-gradient(100deg,#9c9590 0%,#d8d2cc 35%,#efe9e2 55%,#c9b6a4 75%,#8b6a55 100%)}
.search-panel{position:absolute;left:124px;top:230px;width:580px}
.search-title{background:rgba(40,40,40,.78);color:var(--white);font-size:24px;font-weight:700;padding:14px 18px;letter-spacing:.5px}
.search-body{background:rgba(70,70,70,.72);padding:10px 16px 14px}
.search-row{display:flex;gap:10px;align-items:center}
.field{background:var(--white);height:36px;display:flex;align-items:center;gap:8px;padding:0 12px;font-size:13px;color:#555;border-radius:2px}
.field-city{flex:1}
.search-row .btn{height:36px;line-height:36px;padding:0 22px}
.search-row + .search-row{margin-top:10px}
.radio{display:flex;align-items:center;gap:6px;color:var(--white);font-size:13px;font-weight:600}
.radio i{width:12px;height:12px;border-radius:50%;background:var(--white);display:inline-block}
.field-date{width:130px}

/* Section titles */
.section-title{display:flex;align-items:center;justify-content:center;gap:14px;font-size:27px;font-weight:700;color:var(--ink)}
.section-title .accent{color:var(--green)}
.title-rule{display:flex;align-items:center;gap:4px}
.title-rule span{display:block;width:60px;height:2px;background:var(--green)}
.title-rule b{display:block;width:7px;height:7px;border-radius:50%;background:var(--green)}

/* Welcome */
.welcome{position:absolute;top:540px;left:0;width:1200px;height:340px;text-align:center;padding-top:56px}
.welcome p{width:980px;margin:34px auto 0;font-size:12.5px;line-height:22px;color:var(--muted)}
.welcome .btn{margin-top:30px;padding:9px 20px;font-size:13px}

/* How it works */
.how{position:absolute;top:880px;left:0;width:1200px;height:340px;background:var(--beige);padding-top:40px}
.steps{display:flex;justify-content:center;gap:150px;margin-top:36px}
.step{width:180px;text-align:center}
.step-icon{width:96px;height:96px;border-radius:50%;background:var(--white);margin:0 auto;display:flex;align-items:center;justify-content:center;box-shadow:0 0 0 5px #e1ddc9}
.step h3{margin-top:14px;font-size:20px;font-weight:700}
.step-search h3{color:var(--orange)}
.step-book h3{color:var(--green)}
.step-relax h3{color:var(--ink)}
.step p{font-size:12px;line-height:17px;color:var(--ink);margin-top:4px}
.step .more{display:block;margin-top:6px;font-size:12px;font-weight:700}

/* Trust features */
.features{position:absolute;top:1220px;left:0;width:1200px;height:290px;display:flex;justify-content:center;gap:150px;padding-top:30px}
.feature{width:190px;text-align:center}
.feature-photo{width:150px;height:150px;margin:0 auto;border-radius:4px}
.photo-insured{background:linear-gradient(160deg,#f4f1ec,#cdbfa6 70%,#8a7457)}
.photo-vetted{background:linear-gradient(160deg,#f6f4f0,#d8c7ad 65%,#6e5a45)}
.photo-tlc{background:linear-gradient(160deg,#f2efe9,#c9a98a 60%,#5d4636)}
.feature h3{margin-top:14px;font-size:18px;font-weight:700}
.feature p{font-size:12px;line-height:17px;margin-top:4px}

/* Spread the love */
.share{position:absolute;top:1510px;left:0;width:1200px;height:290px}
.share-photo{position:absolute;inset:0;background:linear-gradient(90deg,#8d5a2f 0%,#c98b3f 25%,#e6b25a 45%,#b98a3b 65%,#6f7a2e 100%)}
.share-copy{position:absolute;left:680px;top:70px;color:var(--white)}
.share-copy h2{font-size:42px;font-weight:700}
.share-copy p{font-size:17px;line-height:24px;width:360px;margin-top:2px}
.share-copy .btn{margin-top:16px;padding:8px 16px;font-size:13px}

/* Newsletter */
.newsletter{position:absolute;top:1800px;left:0;width:1200px;height:210px;padding-top:52px}
.newsletter .section-title{font-size:24px}
.signup{display:flex;justify-content:center;gap:14px;margin-top:40px}
.signup .field{width:230px;border:1px solid var(--line);height:34px;color:#999;font-size:12px}
.signup .btn{height:34px;line-height:34px;padding:0 22px;font-size:12px}

/* Footer */
.site-footer{position:absolute;top:2010px;left:0;width:1200px;height:370px;background:var(--footer);color:#ccc;padding:30px 130px 0;display:flex}
.footer-col{width:230px}
.footer-col h4{color:var(--white);font-size:17px;font-weight:700;margin-bottom:16px}
.footer-col li{list-style:none;font-size:12px;line-height:22px}
.quick-contact{width:300px}
.quick-contact .qc-field{height:26px;background:#1e1e1e;border:1px solid #3c3c3c;margin-bottom:8px;font-size:11px;color:#888;padding:5px 8px}
.quick-contact .qc-message{height:54px}
.quick-contact .qc-send{display:inline-block;background:#555;color:var(--white);font-size:11px;padding:5px 16px;margin-left:180px}
.footer-brand{margin-left:auto;padding-top:60px;text-align:center}
.footer-brand .brand{color:#8e8e8e;font-size:30px}
.social{display:flex;justify-content:center;gap:10px;margin-top:22px}
.social span{width:26px;height:26px;border-radius:50%;background:var(--green)}
.social span + span{background:#8e8e8e}
.footer-base{position:absolute;top:2380px;left:0;width:1200px;height:40px;background:var(--footer-base);color:#aaa;font-size:11px;text-align:center;line-height:40px}
</style>
</head>
<body>

<header class="site-header">
  <a class="brand" href="#"><span class="brand-dot"></span>Perumis</a>
  <nav class="main-nav"><a href="#">Find a Sitter</a><a href="#">Become a Sitter</a></nav>
  <nav class="user-nav"><a href="#">How it Works</a><a href="#">Sign Up</a><a class="btn btn-green" href="#">Log In</a></nav>
</header>

<section class="hero">
  <div class="hero-photo" role="img" aria-label="Photo of a smiling woman and a toddler sitting on a wooden floor with a brown puppy in a bright room"></div>
  <form class="search-panel">
    <div class="search-title">FIND A LOVING DOG SITTER</div>
    <div class="search-body">
      <div class="search-row">
        <div class="field field-city">
          <svg width="12" height="16" viewBox="0 0 12 16"><path d="M6 0a6 6 0 0 0-6 6c0 4.5 6 10 6 10s6-5.5 6-10a6 6 0 0 0-6-6zm0 8.5A2.5 2.5 0 1 1 6 3.5a2.5 2.5 0 0 1 0 5z" fill="#6cb33f"/></svg>
          City Or Zip
        </div>
        <a class="btn btn-orange" href="#">Find a Sitter</a>
      </div>
      <div class="search-row">
        <label class="radio"><i></i>Overnight</label>
        <label class="radio"><i></i>Daycare</label>
        <div class="field field-date">
          <svg width="14" height="14" viewBox="0 0 14 14"><rect x="1" y="2" width="12" height="11" fill="none" stroke="#777" stroke-width="1.4"/><path d="M1 5h12M4 0v3M10 0v3" stroke="#777" stroke-width="1.4"/></svg>
          Start Date
        </div>
        <div class="field field-date">
          <svg width="14" height="14" viewBox="0 0 14 14"><rect x="1" y="2" width="12" height="11" fill="none" stroke="#777" stroke-width="1.4"/><path d="M1 5h12M4 0v3M10 0v3" stroke="#777" stroke-width="1.4"/></svg>
          End Date
        </div>
      </div>
    </div>
  </form>
</section>

<section class="welcome">
  <h2 class="section-title"><span class="title-rule"><span></span><b></b></span>Welcome to <span class="accent">Perumis</span><span class="title-rule"><b></b><span></span></span></h2>
  <p>Perumis brings together caring dog owners and trusted local hosts who treat every guest like family. Browse sitter profiles, compare homes, rates and experience, then book and pay online in minutes. Whether you need overnight boarding or a day of play, your dog gets attention, comfort and a safe place to stay while you travel.</p>
  <a class="btn btn-green" href="#">Read More</a>
</section>

<section class="how">
  <h2 class="section-title"><span class="title-rule"><span></span><b></b></span>How Does Perumis work?<span class="title-rule"><b></b><span></span></span></h2>
  <div class="steps">
    <div class="step step-search">
      <div class="step-icon"><svg width="48" height="48" viewBox="0 0 48 48"><circle cx="20" cy="20" r="13" fill="none" stroke="#f26522" stroke-width="5"/><path d="M30 30l12 12" stroke="#f26522" stroke-width="7" stroke-linecap="round"/></svg></div>
      <h3>Search</h3>
      <p>Lorem Ipsum is simply dummy text of the printing and typesetting industry.</p>
      <a class="more" href="#">Find a sitter ›</a>
    </div>
    <div class="step step-book">
      <div class="step-icon"><svg width="46" height="46" viewBox="0 0 46 46"><rect x="4" y="7" width="38" height="35" rx="3" fill="none" stroke="#6cb33f" stroke-width="4"/><path d="M4 16h38M13 2v9M33 2v9" stroke="#6cb33f" stroke-width="4"/><path d="M14 28l6 6 12-12" fill="none" stroke="#6cb33f" stroke-width="4"/></svg></div>
      <h3>Book</h3>
      <p>Lorem Ipsum is simply dummy text of the printing and typesetting industry.</p>
      <a class="more" href="#">More About ›</a>
    </div>
    <div class="step step-relax">
      <div class="step-icon"><svg width="48" height="44" viewBox="0 0 48 44"><rect x="3" y="11" width="42" height="30" rx="4" fill="#333"/><path d="M16 11V5h16v6" fill="none" stroke="#333" stroke-width="4"/><path d="M3 22h42" stroke="#fff" stroke-width="2"/></svg></div>
      <h3>Relax</h3>
      <p>Lorem Ipsum is simply dummy text of the printing and typesetting industry.</p>
      <a class="more" href="#">More About ›</a>
    </div>
  </div>
</section>

<section class="features">
  <div class="feature">
    <div class="feature-photo photo-insured" role="img" aria-label="Photo of a puppy wearing a stethoscope"></div>
    <h3>Insured Pets</h3>
    <p>Lorem Ipsum is simply dummy text of the printing and typesetting</p>
  </div>
  <div class="feature">
    <div class="feature-photo photo-vetted" role="img" aria-label="Photo of a small terrier sitting upright"></div>
    <h3>Vetted Hosts</h3>
    <p>Lorem Ipsum is simply dummy text of the printing and typesetting</p>
  </div>
  <div class="feature">
    <div class="feature-photo photo-tlc" role="img" aria-label="Photo of a small brown puppy resting"></div>
    <h3>One on One TLC</h3>
    <p>Lorem Ipsum is simply dummy text of the printing and typesetting</p>
  </div>
</section>

<section class="share">
  <div class="share-photo" role="img" aria-label="Photo of a woman hugging a white golden retriever outdoors among autumn leaves"></div>
  <div class="share-copy">
    <h2>Spread the Love</h2>
    <p>Lorem Ipsum is simply dummy text of the printing and typesetting industry.</p>
    <a class="btn btn-orange" href="#">Start Sharing</a>
  </div>
</section>

<section class="newsletter">
  <h2 class="section-title"><span class="title-rule"><span></span><b></b></span>Stay in Touch with Perumis <span class="accent">for the Latest Dog Tips</span><span class="title-rule"><b></b><span></span></span></h2>
  <form class="signup">
    <div class="field">Email</div>
    <div class="field">Name</div>
    <a class="btn btn-green" href="#">SUBMIT</a>
  </form>
</section>

<footer class="site-footer">
  <div class="footer-col">
    <h4>Company</h4>
    <ul><li>About Us</li><li>Terms Of Service</li><li>Privacy Policy</li></ul>
  </div>
  <div class="footer-col">
    <h4>Help</h4>
    <ul><li>Support Center</li><li>How Hosting Works</li><li>Contact Us</li></ul>
  </div>
  <div class="footer-col quick-contact">
    <h4>Quick Contact</h4>
    <div class="qc-field">Name</div>
    <div class="qc-field">Email</div>
    <div class="qc-field qc-message">Message</div>
    <span class="qc-send">SEND</span>
  </div>
  <div class="footer-brand">
    <div class="brand"><span class="brand-dot"></span>Perumis</div>
    <div class="social"><span></span><span></span><span></span></div>
  </div>
</footer>
<div class="footer-base">© 2015 Perumis. All Rights Reserved</div>

</body>
</html>
```